Stationery Design Project

KT7 Staffing requires letterhead and business card designs for a company based in London. Just like the name, we're a management resourcing company, providing resources to third party companies. You can see www.kt7staffing-example.com for ideas on existing colour schemes and design concepts that have been implimented and agreed to. Ultimately the design should broadcast professionalism, safety and the concept of growth.

Target Market(s)

Financial institutes; friendly societies (All UK based)

Industry/Entity Type

Safety

Requirements
Must have
• Files produced should be print ready; and the text in them editable (eg address, name etc)

```html
<!DOCTYPE html>
<html lang="en">
<head>
<meta charset="utf-8">
<title>KT7 Staffing — Stationery</title>
<link href="https://fonts.googleapis.com/css2?family=Questrial&display=swap" rel="stylesheet">
<style>
  :root {
    --backdrop: #c4c4c4;
    --page: #ffffff;
    --paper: #ffffff;
    --teal: #1b9dae;
    --teal-dark: #1a8c9c;
    --ink: #333333;
    --shadow: 0 2px 6px rgba(0,0,0,0.35);
  }
  html, body {
    margin: 0; padding: 0;
    width: 1200px; height: 842px;
    overflow: hidden;
    background: var(--page);
    font-family: "Questrial", sans-serif;
  }
  .canvas { position: relative; width: 1200px; height: 842px; }
  .backdrop { position: absolute; left: 0; top: 0; width: 1200px; height: 736px; background: var(--backdrop); }

  .sheet {
    position: absolute;
    background: var(--paper);
    box-shadow: var(--shadow);
    overflow: hidden;
  }
  .brand-name {
    position: absolute;
    margin: 0;
    color: var(--teal-dark);
    font-weight: 400;
    white-space: nowrap;
    line-height: 1;
  }
  .address-band {
    position: absolute;
    left: 0; right: 0; bottom: 0;
    background: var(--teal);
    color: #ffffff;
    font-size: 10.5px;
    white-space: nowrap;
    display: flex;
    align-items: center;
  }

  /* Letterhead */
  .letterhead { left: 23px; top: 28px; width: 527px; height: 682px; }
  .letterhead .brand-name { left: 23px; top: 30px; font-size: 30px; }
  .letterhead .address-band { height: 36px; padding-left: 67px; }

  /* Business card */
  .card { border-radius: 8px; width: 232px; height: 128px; }
  .card-front { left: 762px; top: 64px; background: var(--teal); }
  .card-front .brand-name { color: #ffffff; font-size: 22px; left: 0; right: 0; top: 52px; text-align: center; }
  .card-back { left: 762px; top: 219px; }
  .card-back .contact {
    position: absolute;
    right: 122px; top: 21px;
    text-align: right;
    color: var(--ink);
    font-size: 6px;
    line-height: 1.4;
    white-space: nowrap;
  }
  .card-back .person { font-size: 8.5px; font-weight: 700; color: #222; }
  .card-back .role { color: var(--teal); margin-bottom: 22px; }
  .card-back .gap { margin-top: 7px; }
  .card-back .web { color: var(--teal); font-weight: 700; }
  .card-back .brand-name { left: 122px; top: 57px; font-size: 15px; }

  /* Envelope */
  .envelope { left: 585px; top: 395px; width: 588px; height: 255px; }
  .envelope .brand-name { left: 23px; top: 30px; font-size: 30px; }
  .envelope .address-band { height: 35px; padding-left: 62px; }
</style>
</head>
<body>
<main class="canvas">
  <div class="backdrop"></div>

  <section class="sheet letterhead" aria-label="Letterhead">
    <p class="brand-name">KT7 Staffing</p>
    <footer class="address-band">27 Fennick Row , Suite 4 • Aldmere, London EC9 4ZX, UK • 020-7946-0831</footer>
  </section>

  <section class="sheet card card-front" aria-label="Business card, front">
    <p class="brand-name">KT7 Staffing</p>
  </section>

  <section class="sheet card card-back" aria-label="Business card, back">
    <div class="contact">
      <div class="person">Daniel Hartley</div>
      <div class="role">manager</div>
      <div>City, State Name</div>
      <div>31 StreetName str.</div>
      <div class="gap">020-7946-0155</div>
      <div>hello@kt7staffing-example.com</div>
      <div class="web">www.kt7staffing-example.com</div>
    </div>
    <p class="brand-name">KT7 Staffing</p>
  </section>

  <section class="sheet envelope" aria-label="Envelope">
    <p class="brand-name">KT7 Staffing</p>
    <footer class="address-band">27 Fennick Row , Suite 4 • Aldmere, London EC9 4ZX, UK</footer>
  </section>

</main>
</body>
</html>
```